Spring Detox sale graphics for social media

You MUST read the Brief in the WORD document and follow the instructions there. I want to create 10 social media graphics (new Instagram size 4:5 (1080 x 1350 pixels) focusing on our Mother’s Day Spring Detox Sale graphics, using any of the pics attached. Use the attached pics, NO RANDOM STOCK PHOTOGRAPHY. For the color scheme of the graphics, they should all be complementary to the product colors or feel like Spring time.

Target Market(s)

primarily women

Requirements
Must have
• the photos and text attached

```html
<!DOCTYPE html>
<html lang="en">
<head>
<meta charset="utf-8">
<title>Mother's Day Spring Detox Sale – Social Set</title>
<link rel="stylesheet" href="https://fonts.googleapis.com/css2?family=Oswald:wght@400;500;600;700&family=Roboto+Slab:wght@500;700&family=Great+Vibes&family=Montserrat:wght@400;600;700;800&family=Dancing+Script:wght@600;700&display=swap">
<style>
:root{
  --pink:#e8437c;
  --rose:#c9416f;
  --blush:#fbe3ea;
  --green:#4f8f3a;
  --lime:#b7d564;
  --teal:#3ea69c;
  --navy:#27407e;
  --purple:#8459a8;
  --lavender:#a993cf;
  --gold:#b8963a;
  --forest:#2e5a4c;
  --ink:#2c2a2e;
  --white:#ffffff;
}
*{margin:0;padding:0;box-sizing:border-box}
html,body{width:1200px;height:561px;overflow:hidden;background:var(--white)}
body{position:relative;font-family:'Montserrat',sans-serif}
.card{position:absolute;width:183px;height:229px;overflow:hidden;box-shadow:0 2px 6px rgba(0,0,0,.12)}
.r1{top:36px}.r2{top:295px}
.c1{left:80px}.c2{left:298px}.c3{left:516px}.c4{left:733px}.c5{left:950px}
.abs{position:absolute;white-space:nowrap}
.ctr{left:0;right:0;text-align:center}
.osw{font-family:'Oswald',sans-serif}
.script{font-family:'Great Vibes',cursive}
.dscript{font-family:'Dancing Script',cursive}
.slab{font-family:'Roboto Slab',serif}
.photo{position:absolute}
.model{border-radius:2px;background:linear-gradient(180deg,#f3d6df 0%,#6b5048 14%,#8a6a5c 26%,#f2f0f1 38%,#ece9ec 55%,#2a2a30 62%,#1f1f25 100%)}
.products{border-radius:4px;background:linear-gradient(180deg,rgba(255,255,255,.9),rgba(232,234,240,.95))}
.flowers{border-radius:50%;background:radial-gradient(circle,rgba(244,150,182,.85),rgba(248,200,216,.55) 55%,rgba(248,200,216,0) 72%)}
.leaves{border-radius:50%;background:radial-gradient(circle,rgba(140,190,130,.6),rgba(170,210,160,.25) 55%,rgba(170,210,160,0) 72%)}
.marble{background:linear-gradient(180deg,#f7f6f6,#e6e3e5)}
.band{position:absolute;left:0;right:0;display:flex;align-items:center;justify-content:center;white-space:nowrap}
.icons{display:flex;justify-content:space-around;align-items:center}
.icon{display:flex;flex-direction:column;align-items:center;font-size:3.2px;line-height:1.2;text-align:center;font-weight:600}
.icon svg{width:9px;height:9px;margin-bottom:1px}
</style>
</head>
<body>

<!-- 1 -->
<section class="card r1 c1" style="background:linear-gradient(160deg,#fbf6ec,#f5f1e8 50%,#eadfe4)">
  <div class="photo flowers" role="img" aria-label="Cherry blossom branch" style="left:-10px;top:-14px;width:90px;height:50px"></div>
  <div class="photo leaves" role="img" aria-label="Eucalyptus leaves" style="left:110px;top:-12px;width:90px;height:50px"></div>
  <div class="photo leaves" role="img" aria-label="Eucalyptus sprig" style="left:-20px;top:90px;width:40px;height:90px"></div>
  <div class="photo leaves" role="img" aria-label="Eucalyptus sprig" style="left:160px;top:90px;width:40px;height:90px"></div>
  <div class="photo" role="img" aria-label="Mint and blush watercolour marble wash" style="left:0;top:130px;width:183px;height:99px;background:linear-gradient(100deg,rgba(170,215,200,.45),rgba(245,240,235,.2) 45%,rgba(232,180,195,.55))"></div>
  <div class="abs ctr slab" style="top:36px;font-size:16px;color:var(--rose);font-weight:700">MOTHER'S DAY</div>
  <div class="abs ctr slab" style="top:56px;font-size:14px;color:var(--rose);font-weight:700">SPRING <span style="color:var(--gold)">DETOX</span> SALE</div>
  <div class="abs ctr osw" style="top:77px;font-size:7px;color:var(--gold)">SPRING RESET. SUMMER READY</div>
  <div class="abs ctr osw" style="top:89px;font-size:13px;color:var(--ink);font-weight:500">25% OFF EVERYTHING</div>
  <div class="photo products" role="img" aria-label="Four supplement bottles on a marble pedestal" style="left:32px;top:126px;width:121px;height:72px"></div>
  <div class="abs" style="left:60px;top:204px;width:63px;height:12px;background:var(--gold);color:#fff;font-size:7px;font-weight:600;display:flex;align-items:center;justify-content:center">SHOP THE SALE</div>
</section>

<!-- 2 -->
<section class="card r1 c2" style="background:linear-gradient(180deg,#fbe0e8,#f7d3de)">
  <div class="photo flowers" role="img" aria-label="Cherry blossom branches" style="left:120px;top:-20px;width:90px;height:70px"></div>
  <div class="photo flowers" role="img" aria-label="Pink tulips" style="left:-20px;top:150px;width:70px;height:70px"></div>
  <div class="photo model" role="img" aria-label="Smiling woman in white crop top and black pants" style="left:108px;top:34px;width:66px;height:150px"></div>
  <div class="photo marble" style="left:0;top:198px;width:183px;height:31px"></div>
  <div class="abs osw" style="left:22px;top:2px;font-size:35px;color:var(--pink);font-weight:700;line-height:1">25%</div>
  <div class="abs osw" style="left:26px;top:35px;font-size:30px;color:var(--pink);font-weight:700;line-height:1">OFF</div>
  <div class="abs script" style="left:23px;top:67px;font-size:15px;color:var(--rose)">Mother's Day</div>
  <div class="abs osw" style="left:22px;top:84px;font-size:27px;color:var(--pink);font-weight:700;line-height:1">SPRING</div>
  <div class="abs osw" style="left:19px;top:112px;font-size:17px;color:var(--green);font-weight:700;line-height:1">DETOX SALE</div>
  <div class="abs dscript" style="left:40px;top:133px;width:60px;height:13px;background:var(--pink);color:#fff;font-size:10px;text-align:center;transform:rotate(-8deg)">Everything!</div>
  <div class="abs osw" style="left:50px;top:157px;font-size:5px;color:var(--green);text-align:center;line-height:1.2">SPRING CLEANSE.<br>SUMMER GLOW</div>
  <div class="photo products" role="img" aria-label="Row of supplement bottles and serums" style="left:38px;top:170px;width:140px;height:36px"></div>
  <div class="band osw" style="top:212px;height:10px;font-size:5px;color:var(--pink)">♥&nbsp; DETOX THIS SPRING. SHINE THIS SUMMER.</div>
</section>

<!-- 3 -->
<section class="card r1 c3" style="background:linear-gradient(180deg,#fbe5ec,#f9dde6)">
  <div class="photo flowers" role="img" aria-label="Pink peony" style="left:-15px;top:70px;width:50px;height:60px"></div>
  <div class="photo leaves" role="img" aria-label="Green leaves" style="left:-20px;top:30px;width:40px;height:60px"></div>
  <div class="photo flowers" role="img" aria-label="Blossom branch" style="left:150px;top:0;width:50px;height:70px"></div>
  <div class="photo flowers" role="img" aria-label="Pink peony" style="left:155px;top:120px;width:45px;height:55px"></div>
  <div class="abs ctr script" style="top:4px;font-size:20px;color:var(--pink)">Mother's Day</div>
  <div class="abs ctr script" style="top:24px;font-size:20px;color:var(--green)">Spring Detox</div>
  <div class="abs osw" style="left:38px;top:50px;font-size:56px;color:var(--pink);font-weight:700;line-height:1">25<span style="font-size:36px">%</span></div>
  <div class="abs osw" style="left:117px;top:82px;font-size:24px;color:var(--pink);font-weight:700;line-height:1">OFF</div>
  <div class="abs ctr osw" style="top:116px;font-size:18px;color:var(--navy);font-weight:600">ALL SUPPLEMENTS</div>
  <div class="band" style="top:139px;left:28px;right:28px;height:8px;background:var(--pink);color:#fff;font-size:5px;font-weight:700;letter-spacing:1px">SPRING DETOX SALE!</div>
  <div class="abs ctr" style="top:150px;font-size:3.5px;font-weight:700;color:var(--navy);letter-spacing:.3px">DETOX • REBALANCE • REFRESH • FEEL AMAZING</div>
  <div class="photo products" role="img" aria-label="Four supplement bottles in a row" style="left:22px;top:158px;width:140px;height:64px"></div>
</section>

<!-- 4 -->
<section class="card r1 c4" style="background:linear-gradient(180deg,#faf6e6,#f3d9e3 55%,#d8c4ec)">
  <div class="abs ctr" style="top:2px;font-size:15px;font-weight:600;color:var(--purple);line-height:1.1"><b style="color:var(--pink)">25%</b> SPRING<br><b style="color:var(--pink)">OFF</b> DETOX</div>
  <div class="abs ctr" style="top:32px;font-size:34px;font-weight:800;color:var(--pink);line-height:1">SALE</div>
  <div class="abs ctr" style="top:70px;font-size:7px;font-weight:700;color:var(--pink)">SPRING RESET. SUMMER READY</div>
  <div class="photo leaves" role="img" aria-label="Floating green leaves" style="left:10px;top:125px;width:40px;height:40px"></div>
  <div class="photo leaves" role="img" aria-label="Floating green leaves" style="left:140px;top:180px;width:40px;height:30px"></div>
  <div class="photo products" role="img" aria-label="Four floating supplement bottles" style="left:20px;top:90px;width:143px;height:108px;background:linear-gradient(180deg,rgba(255,255,255,.7),rgba(235,230,242,.6))"></div>
  <div class="band" style="top:208px;height:21px;background:var(--lime);color:var(--ink);font-size:12px;font-weight:600;letter-spacing:.5px">MOTHER'S DAY</div>
</section>

<!-- 5 -->
<section class="card r1 c5" style="background:linear-gradient(180deg,#fbe4ec,#f7dbe3)">
  <div class="photo model" role="img" aria-label="Smiling woman in white crop top" style="left:110px;top:18px;width:68px;height:165px"></div>
  <div class="photo flowers" role="img" aria-label="White and pink tulips" style="left:-15px;top:150px;width:60px;height:70px"></div>
  <div class="photo marble" style="left:0;top:205px;width:183px;height:24px"></div>
  <div class="abs" style="left:7px;top:1px;width:85px;height:60px;background:#f49bb8"></div>
  <div class="abs" style="left:18px;top:8px;font-size:31px;font-weight:800;color:#fff;line-height:1">25<span style="font-size:20px">%</span></div>
  <div class="abs" style="left:78px;top:32px;font-size:7px;font-weight:700;color:#fff">OFF</div>
  <div class="abs" style="left:20px;top:48px;font-size:8px;font-weight:700;color:var(--rose)">EVERYTHING!</div>
  <div class="abs" style="left:7px;top:70px;font-size:9.5px;font-weight:600;color:var(--pink);letter-spacing:.3px">MOTHER'S DAY</div>
  <div class="abs" style="left:7px;top:87px;font-size:9.5px;font-weight:600;color:var(--pink);letter-spacing:.3px">SPRING DETOX</div>
  <div class="abs" style="left:6px;top:101px;font-size:30px;font-weight:800;color:var(--pink);line-height:1">SALE</div>
  <div class="photo products" role="img" aria-label="Row of supplement bottles" style="left:30px;top:160px;width:148px;height:46px"></div>
  <div class="abs ctr" style="top:213px;font-size:8px;font-weight:700;color:var(--pink);letter-spacing:.5px">REFRESH YOUR BODY</div>
</section>

<!-- 6 -->
<section class="card r2 c1" style="background:linear-gradient(180deg,#fdf4f6,#f5eef0)">
  <div class="photo flowers" role="img" aria-label="Pink blossoms" style="left:140px;top:-10px;width:60px;height:50px"></div>
  <div class="photo flowers" role="img" aria-label="Pink blossoms" style="left:-15px;top:85px;width:45px;height:70px"></div>
  <div class="photo model" role="img" aria-label="Smiling woman pointing at products" style="left:98px;top:20px;width:76px;height:130px"></div>
  <div class="photo marble" style="left:0;top:150px;width:183px;height:40px"></div>
  <div class="abs osw" style="left:30px;top:4px;font-size:6.5px;color:var(--pink);font-weight:500">25% OFF EVERYTHING!</div>
  <div class="abs script" style="left:30px;top:12px;font-size:13px;color:var(--rose)">Mother's Day</div>
  <div class="abs osw" style="left:28px;top:32px;font-size:31px;color:var(--green);font-weight:700;line-height:1">SALE</div>
  <div class="abs osw" style="left:38px;top:66px;font-size:24px;color:var(--pink);font-weight:700;line-height:1">FEEL</div>
  <div class="abs script" style="left:18px;top:95px;width:68px;height:11px;background:var(--pink);color:#fff;font-size:9px;text-align:center;line-height:11px">Amazing Again ♥</div>
  <div class="abs" style="left:24px;top:109px;font-size:4.5px;color:var(--ink)">CLEANSE. RESET. RENEW</div>
  <div class="photo products" role="img" aria-label="Supplements and serums on marble counter" style="left:28px;top:135px;width:140px;height:46px"></div>
  <div class="abs icons" style="left:15px;right:15px;top:189px;color:var(--ink)">
    <div class="icon"><svg viewBox="0 0 10 10"><circle cx="5" cy="5" r="4.5" fill="var(--pink)"/></svg>CLEANSE<br>Detox toxins</div>
    <div class="icon"><svg viewBox="0 0 10 10"><circle cx="5" cy="5" r="4.5" fill="var(--pink)"/></svg>RESET<br>Rebalance</div>
    <div class="icon"><svg viewBox="0 0 10 10"><circle cx="5" cy="5" r="4.5" fill="var(--pink)"/></svg>RENEW<br>Boost energy</div>
    <div class="icon"><svg viewBox="0 0 10 10"><circle cx="5" cy="5" r="4.5" fill="var(--pink)"/></svg>FEEL YOUR<br>BEST</div>
  </div>
  <div class="band" style="top:217px;left:14px;right:14px;height:8px;background:var(--pink);color:#fff;font-size:4.2px">25% OFF MOTHER'S DAY SALE: FEEL AMAZING AGAIN! ♥</div>
</section>

<!-- 7 -->
<section class="card r2 c2" style="background:linear-gradient(180deg,#fbe8ee,#f6e0e7)">
  <div class="photo model" role="img" aria-label="Smiling woman in white crop top" style="left:112px;top:18px;width:64px;height:140px"></div>
  <div class="photo flowers" role="img" aria-label="Pink tulips" style="left:-15px;top:160px;width:50px;height:60px"></div>
  <div class="photo flowers" role="img" aria-label="Pink tulips" style="left:145px;top:170px;width:50px;height:60px"></div>
  <div class="photo marble" style="left:0;top:152px;width:183px;height:38px"></div>
  <div class="band" style="top:0;left:12px;right:12px;height:11px;background:#f3a7bf;color:#fff;font-size:4.5px;letter-spacing:1.5px;border-radius:6px">THIS MOTHER'S DAY</div>
  <div class="abs" style="left:27px;top:14px;width:62px;height:27px;border:1px solid var(--pink);border-radius:3px;text-align:center">
    <div class="osw" style="font-size:14px;color:var(--pink);font-weight:500;line-height:1.2">25% OFF</div>
    <div style="font-size:4.3px;color:var(--ink)">MOTHER'S DAY SALE</div>
  </div>
  <div class="abs osw" style="left:24px;top:45px;font-size:22px;color:var(--pink);font-weight:700;line-height:1.1">REFRESH</div>
  <div class="abs osw" style="left:28px;top:71px;font-size:30px;color:var(--forest);font-weight:700;line-height:1">YOUR</div>
  <div class="abs script" style="left:30px;top:98px;font-size:29px;color:var(--pink);line-height:1">Body</div>
  <div class="abs" style="top:134px;left:20px;width:80px;text-align:center;font-size:4.8px;color:var(--pink)">CLEANSE. RESET. THRIVE.</div>
  <div class="abs" style="top:141px;left:20px;width:80px;text-align:center;font-size:3.3px;color:var(--ink);line-height:1.2">Support her wellness journey<br>inside and out.</div>
  <div class="photo products" role="img" aria-label="Row of supplements and serums" style="left:25px;top:154px;width:150px;height:34px"></div>
  <div class="abs icons" style="left:30px;right:30px;top:197px;color:var(--pink)">
    <div class="icon"><svg viewBox="0 0 10 10"><circle cx="5" cy="5" r="4.3" fill="none" stroke="var(--forest)"/></svg>CLEANSE<br>NATURALLY</div>
    <div class="icon"><svg viewBox="0 0 10 10"><circle cx="5" cy="5" r="4.3" fill="none" stroke="var(--forest)"/></svg>RESET<br>YOUR BODY</div>
    <div class="icon"><svg viewBox="0 0 10 10"><circle cx="5" cy="5" r="4.3" fill="none" stroke="var(--forest)"/></svg>THRIVE<br>EVERY DAY</div>
  </div>
</section>

<!-- 8 -->
<section class="card r2 c3" style="background:linear-gradient(180deg,#fdf3f5,#f7e9ee)">
  <div class="photo flowers" role="img" aria-label="Pink tulips" style="left:150px;top:10px;width:50px;height:80px"></div>
  <div class="photo flowers" role="img" aria-label="Pink tulips and greenery" style="left:-15px;top:140px;width:50px;height:70px"></div>
  <div class="photo model" role="img" aria-label="Smiling woman in white crop top" style="left:110px;top:14px;width:64px;height:140px"></div>
  <div class="abs" style="left:20px;top:3px;font-size:8px;color:var(--pink);letter-spacing:2px">MOTHER'S DAY</div>
  <div class="abs osw" style="left:22px;top:11px;font-size:13px;color:var(--green);letter-spacing:3px">25% OFF</div>
  <div class="abs osw" style="left:9px;top:30px;font-size:24px;color:var(--pink);font-weight:700;letter-spacing:2px;line-height:1">SPRING</div>
  <div class="abs" style="left:8px;top:58px;font-size:24px;color:var(--purple);font-weight:800;line-height:1">DETOX</div>
  <div class="abs script" style="left:35px;top:84px;font-size:27px;color:var(--green);line-height:1">Sale</div>
  <div class="abs osw" style="left:12px;top:116px;width:92px;height:9px;background:var(--pink);color:#fff;font-size:5px;text-align:center;line-height:9px;border-radius:2px">SPRING CLEANSE. SUMMER GLOW</div>
  <div class="abs" style="left:15px;top:128px;font-size:4.8px;color:var(--ink);line-height:1.3">Refresh your body.<br>Reclaim your energy.<br>Feel your best this Spring.</div>
  <div class="photo products" role="img" aria-label="Supplements and serums among pink tulips" style="left:18px;top:152px;width:160px;height:56px"></div>
  <div class="band icons" style="top:211px;height:17px;background:var(--green);color:#fff">
    <div style="font-size:3.6px">NATURAL<br>INGREDIENTS</div>
    <div style="font-size:3.6px">HORMONE<br>BALANCE</div>
    <div style="font-size:3.6px">TOTAL BODY<br>WELLNESS</div>
  </div>
</section>

<!-- 9 -->
<section class="card r2 c4" style="background:linear-gradient(180deg,#fdf6f8,#f6eef1)">
  <div class="photo flowers" role="img" aria-label="Pink roses" style="left:-15px;top:150px;width:55px;height:60px"></div>
  <div class="photo flowers" role="img" aria-label="Pink roses" style="left:150px;top:160px;width:45px;height:50px"></div>
  <div class="photo model" role="img" aria-label="Smiling woman in white crop top" style="left:100px;top:10px;width:74px;height:150px"></div>
  <div class="abs osw" style="left:22px;top:2px;font-size:19px;color:var(--pink);font-weight:500">25% OFF</div>
  <div class="abs script" style="left:20px;top:23px;font-size:15px;color:var(--pink)">Mother's Day</div>
  <div class="abs script" style="left:30px;top:39px;font-size:23px;color:var(--pink)">Sale</div>
  <div class="abs osw" style="left:8px;top:65px;font-size:16px;color:var(--teal);font-weight:500">DETOX THIS</div>
  <div class="abs osw" style="left:14px;top:84px;font-size:25px;color:var(--teal);font-weight:600;line-height:1.1">SPRING</div>
  <div class="abs" style="left:22px;top:117px;width:67px;height:9px;background:var(--teal);color:#fff;font-size:5.2px;text-align:center;line-height:9px">SHINE THIS SUMMER</div>
  <div class="abs" style="left:37px;top:131px;width:36px;height:30px;border-radius:50%;background:#fbdbe5;color:var(--pink);font-size:4.6px;font-weight:700;display:flex;align-items:center;justify-content:center;text-align:center;line-height:1.2">CLEANSE.<br>RESET.<br>GLOW.</div>
  <div class="photo products" role="img" aria-label="Row of supplements with roses" style="left:14px;top:162px;width:162px;height:38px"></div>
  <div class="band icons" style="top:202px;height:12px;background:#8fd0c7;color:#fff;font-size:3.8px;padding:0 30px">
    <span>DETOX</span><span>RENEW</span><span>FEEL AMAZING</span>
  </div>
  <div class="band" style="top:216px;height:12px;background:#fbd7e2;color:var(--pink);font-size:4.3px;font-weight:600">SUPPORT HER WELLNESS JOURNEY INSIDE AND OUT. ♥</div>
</section>

<!-- 10 -->
<section class="card r2 c5" style="background:linear-gradient(180deg,#fbf4f5,#f1ece9)">
  <div class="photo flowers" role="img" aria-label="Pink gerbera daisy" style="left:-20px;top:95px;width:60px;height:60px"></div>
  <div class="photo leaves" role="img" aria-label="Green grass and stems" style="left:-20px;top:30px;width:40px;height:80px"></div>
  <div class="photo flowers" role="img" aria-label="Pink tulips" style="left:150px;top:100px;width:45px;height:70px"></div>
  <div class="photo leaves" role="img" aria-label="Green leaves" style="left:155px;top:30px;width:40px;height:70px"></div>
  <div class="abs ctr osw" style="top:6px;font-size:17px;color:var(--pink);font-weight:500">25% OFF</div>
  <div class="abs ctr" style="top:28px;font-size:8.5px;color:var(--purple)">MOTHER'S DAY</div>
  <div class="abs ctr script" style="top:37px;font-size:38px;color:var(--purple);line-height:1">Sale</div>
  <div class="abs ctr" style="top:82px;font-size:19px;color:var(--green);font-weight:800;line-height:1">SPRING</div>
  <div class="abs ctr" style="top:103px;font-size:19px;color:var(--pink);font-weight:800;line-height:1">DETOX</div>
  <div class="abs ctr" style="top:127px;font-size:6.5px;color:var(--teal);font-weight:700">FOR A SUMMER BODY</div>
  <div class="photo products" role="img" aria-label="Four supplement bottles on a ledge" style="left:25px;top:138px;width:133px;height:62px"></div>
  <div class="band icons" style="top:205px;height:24px;background:var(--lavender);color:#fff;padding:0 14px">
    <div class="icon"><svg viewBox="0 0 10 10"><circle cx="5" cy="5" r="4.3" fill="none" stroke="#fff"/></svg>CLEANSE</div>
    <div class="icon"><svg viewBox="0 0 10 10"><circle cx="5" cy="5" r="4.3" fill="none" stroke="#fff"/></svg>BALANCE</div>
    <div class="icon"><svg viewBox="0 0 10 10"><circle cx="5" cy="5" r="4.3" fill="none" stroke="#fff"/></svg>RENEW</div>
    <div class="icon"><svg viewBox="0 0 10 10"><path d="M5 8.5 1.5 5A2 2 0 0 1 5 2.5 2 2 0 0 1 8.5 5Z" fill="none" stroke="#fff"/></svg>FEEL YOUR BEST</div>
  </div>
</section>

</body>
</html>
```